Redesign of the company website and content pages

Re design our company website to move it away from the black theme and make it fresher and cleaner and improve the overall design. The header area needs a new creative approach, which i have shown an example of in the documentation of the kind of thing that might be of interest, but please be creative, I am not expecting to see replication or newer iterations of the current site we have, i would like a fresh and stunning looking clean site with plenty of space. Creative use of the logo would also be welcomed, for the header area and buttons (potentially).

The internal page design should be for the staff images page, so again creative approach to this would also be appreciated.

Please feel free to contact me with any questions of guidance. Files should be provided in layered psd format at the end of the project.

Industry/Entity Type

It Company

```html
<!DOCTYPE html>
<html lang="en">
<head>
<meta charset="utf-8">
<title>Pondera – Digital Agency</title>
<link rel="stylesheet" href="https://fonts.googleapis.com/css2?family=Source+Sans+3:ital,wght@0,400;0,600;1,400&family=Noto+Sans:wght@400;700&family=Source+Code+Pro:wght@600&family=Roboto+Condensed:wght@400&display=swap">
<style>
:root{
  --bg:#e9ebec;
  --panel:#ffffff;
  --blue:#0099d8;
  --blue-text:#0a8fd0;
  --ink:#4a4a4a;
  --muted:#7a7a7a;
  --rule:#cfcfcf;
  --box-line:#c9c9c9;
  --dark:#1d1d1d;
}
*{margin:0;padding:0;box-sizing:border-box}
html,body{width:1200px;height:942px;overflow:hidden}
body{
  position:relative;
  background:radial-gradient(ellipse at 30% 40%,#f6f7f8 0%,var(--bg) 70%);
  font-family:"Noto Sans",sans-serif;color:var(--ink);
}
.page{
  position:absolute;left:137px;top:10px;width:930px;height:932px;
  background:var(--panel);border-radius:30px 30px 0 0;
  box-shadow:0 0 14px rgba(0,0,0,.06);
}
.abs{position:absolute}
.contact{right:55px;top:14px;font:400 14px "Source Sans 3",sans-serif;color:var(--muted)}
.contact b{color:var(--blue);font-weight:600}
.contact span+span{margin-left:8px}
.brand{left:56px;top:38px;display:flex;align-items:center;gap:10px}
.brand-dot{width:34px;height:34px;border-radius:50%;background:var(--blue)}
.brand-name{font:400 42px "Source Sans 3",sans-serif;color:var(--dark);letter-spacing:-.5px}
.nav{right:58px;top:60px;display:flex;font:400 15px "Source Sans 3",sans-serif;color:#8a8a8a}
.nav a{color:inherit;text-decoration:none}
.nav a+a::before{content:"|";margin:0 15px 0 16px;color:#aaa}
.hero{left:56px;top:126px;width:816px;height:200px;display:flex}
.hero-visual{
  width:517px;height:200px;position:relative;
  background:linear-gradient(180deg,#e4e4e4 0%,#f7f7f7 60%,#e9e9e9 100%);
}
.hero-phones{position:absolute;left:30px;top:14px;width:195px;height:170px;border-radius:14px;
  background:linear-gradient(90deg,#2a2a2a,#4a4a4a 50%,#2a2a2a)}
.hero-tag{position:absolute;left:255px;top:34px;font-family:"Roboto Condensed",sans-serif;color:#3a3a3a;line-height:1}
.hero-tag small{display:block;font-size:17px}
.hero-tag strong{display:block;font-size:29px;font-weight:400;margin-top:2px}
.hero-quote{
  width:299px;background:var(--blue);color:#fff;padding:33px 30px 0 34px;
  font:italic 400 15px/21px "Source Sans 3",sans-serif;
}
.divider-v{left:572px;top:336px;height:550px;border-left:1px dashed var(--rule)}
.divider-h{border-top:1px dashed var(--rule)}
h2{font:400 18px "Source Sans 3",sans-serif;color:#555}
.intro{left:61px;top:355px;width:470px}
.intro p{margin-top:8px;font-size:12px;line-height:21px;color:#555}
.service{left:61px;width:475px;height:77px;border:1px solid var(--box-line);padding:9px 12px}
.service h3{font:400 17px "Noto Sans",sans-serif;color:#777;letter-spacing:.3px}
.service p{font-size:12px;line-height:17px;color:var(--blue-text);width:292px;margin-top:1px;letter-spacing:.2px}
.service .thumb{position:absolute;right:11px;top:12px;width:167px;height:50px;border:1px solid #e0e0e0;
  box-shadow:1px 2px 2px rgba(0,0,0,.15)}
.feed{left:608px;top:355px;width:260px}
.tweet{font-size:11px;line-height:14px;color:#555;margin-top:13px}
.tweet a,.posts a{color:var(--blue-text);text-decoration:none}
.date{display:block;font:600 10px/14px "Source Code Pro",monospace;color:#333;letter-spacing:.5px}
.posts{left:608px;top:642px;width:260px}
.posts li{list-style:none;font-size:11.5px;line-height:13px;font-weight:700;margin-top:2px}
.posts li:first-child{margin-top:14px}
.ask{left:61px;top:832px}
.ask label{display:flex;align-items:center;gap:5px;margin-top:8px;font-size:12px;color:#666}
.select{width:143px;height:18px;border:1px solid #aaa;position:relative}
.select::after{content:"";position:absolute;right:5px;top:6px;border:4px solid transparent;border-top-color:#222}
.go{color:var(--blue);font-weight:700;font-size:14px;margin-left:6px;letter-spacing:-1px}
.partner{left:631px;top:836px;font:italic 700 16px/24px "Noto Sans",sans-serif;color:var(--blue-text);letter-spacing:1px}
.partner::before{content:"\201C";position:absolute;left:-22px;top:-10px;font:400 40px serif;color:#ccc}
.footer{left:0;top:918px;width:930px;text-align:center;font-size:10px;color:#888;letter-spacing:.4px}
.footer span{margin-left:20px}
</style>
</head>
<body>
<div class="page">
  <div class="abs contact"><span><b>T:</b> +44 (0) 20 7946 0321</span><span><b>E:</b> info@pondera-studio.com</span></div>
  <div class="abs brand"><div class="brand-dot"></div><div class="brand-name">pondera</div></div>
  <nav class="abs nav"><a>Home</a><a>Who we are</a><a>What we do</a><a>Case Studies</a><a>Work for us</a><a>Get in touch</a></nav>

  <section class="abs hero">
    <div class="hero-visual">
      <div class="hero-phones" role="img" aria-label="Three smartphones showing film artwork"></div>
      <div class="hero-tag"><small>the next generation of</small><strong>digital design</strong></div>
    </div>
    <blockquote class="hero-quote">“Quote. Aliquam eros leo, pretium at imperdiet id, fringilla at velit. Donec pellentesque mollis massa eu porttitor. Aliquam risus metus, placerat at ornare id”</blockquote>
  </section>

  <div class="abs divider-v"></div>

  <section class="abs intro">
    <h2>Welcome to Pondera!</h2>
    <p>Pondera is a rapidly growing digital agency based in the heart of Soho in central London. We specialise in a range of services across the full digital spectrum, including:</p>
  </section>

  <article class="abs service" style="top:458px">
    <h3>PPC</h3><p>Our team of PPC specialists can help increase your traffic &amp; sales</p>
    <svg class="thumb" viewBox="0 0 167 50" role="img" aria-label="Rising traffic line chart">
      <rect width="167" height="50" fill="#f7f7f7"/>
      <polyline points="76,46 96,34 108,40 128,18 138,26 158,4" fill="none" stroke="#1a9ad6" stroke-width="4"/>
    </svg>
  </article>
  <article class="abs service" style="top:544px">
    <h3>SEO</h3><p>Let our SEO experts help improve your position on Searchly</p>
    <div class="thumb" role="img" aria-label="Search engine illustration with ladder" style="background:linear-gradient(90deg,#dfe7f3,#f4e6d8)"></div>
  </article>
  <article class="abs service" style="top:630px">
    <h3>Social Media</h3><p>Talk directly to your customers – on platforms your customers control!</p>
    <div class="thumb" role="img" aria-label="Row of social network icons" style="background:linear-gradient(90deg,#dce8f2,#f1ece6)"></div>
  </article>
  <article class="abs service" style="top:716px">
    <h3>Email Marketing</h3><p>Target &amp; capture new customers with a specially tailored email campaign</p>
    <div class="thumb" role="img" aria-label="Folder and envelope illustration" style="background:linear-gradient(90deg,#f3c27a,#eeeef2)"></div>
  </article>

  <section class="abs feed">
    <h2>@PonderaDigital</h2>
    <p class="tweet">RT <a>@TheBrandGuild</a> Brand Guild Blog: Future of Marketing, Sir Alan Ward - The Brand Guild.. <a>http://sho.rt/bBj9oG</a><span class="date">2010/06/07</span></p>
    <p class="tweet">RT <a>@TheBrandGuild</a> Are you a true Brand Leader? <a>http://sho.rt/agzsbj</a><span class="date">2010/06/03</span></p>
    <p class="tweet">RT <a>@TheBrandGuild</a> Mobilising the electorate <a>http://sho.rt/9OoUMA</a><span class="date">2010/06/02</span></p>
    <p class="tweet">New on Pondera-studio.com : Chatterly's Final Privacy Update <a>http://www.pondera-studio.com/ chatterly-final-privacy-update/</a><span class="date">2010/05/27</span></p>
  </section>
  <div class="abs divider-h" style="left:573px;top:632px;width:318px"></div>

  <section class="abs posts">
    <h2>Recent Posts</h2>
    <ul>
      <li><a>Chatterly's Final Privacy Update</a><span class="date">2010-05-27</span></li>
      <li><a>New Brand Guild Blog</a><span class="date">2010-05-06</span></li>
      <li><a>Orchard sell's one million Slates</a><span class="date">2010-05-04</span></li>
    </ul>
  </section>

  <div class="abs divider-h" style="left:0;top:822px;width:930px"></div>
  <section class="abs ask">
    <h2>Ask Pondera's Digital specialists any Question</h2>
    <label>Topic: <span class="select"></span><span class="go">&gt;&gt;</span></label>
  </section>
  <p class="abs partner">The Brand Guild's<br>Social Media Partner</p>
  <div class="abs divider-h" style="left:0;top:898px;width:930px"></div>
  <footer class="abs footer">© 2010 Pondera London Limited. All Rights Reserved <span>Privacy Policy | Sitemap | Login</span></footer>
</div>
</body>
</html>
```